Natural Medicine & Health/Fitness Coaching studio requires web page

Require a innovative web page for a studio that coaches clients to better health, nutrition and fitness. The studio compromises of Clinical Nutritionists, Naturopaths, Rehab Trainers, Personal Trainers and Sport Coaches. Would like to see earthy but bold designs emphasizing nutritional health and athletic performance.
Updates

Design only launched today.

Target Market(s)

All genders from 20's to 60's, as well as families

Industry/Entity Type

Nutritionist

Coding

Coded - Design and coding required

Number of Pages Required

3 page

Colors
abd037
3277b5
fbee3d
fece3e
33b8a4
f04a50

Requirements
Must have
• Online booking system, ability to message
• Home page
• Coaching/Fitness page
• Nutritional Medicine page
• Must be suitable for both Fitness and Nutrition

```html
<!DOCTYPE html>
<html lang="en">
<head>
<meta charset="utf-8">
<title>Verdant Fit – Nutritional Therapy</title>
<link href="https://fonts.googleapis.com/css2?family=Roboto:wght@300;400;500;700;900&display=swap" rel="stylesheet">
<style>
:root{
  --green:#a4c93a;
  --green-dark:#8db22c;
  --blue:#3277b5;
  --ink:#2b2b2b;
  --text:#666;
  --muted:#999;
  --light:#f2f2f2;
  --line:#e2e2e2;
  --footer:#2d2d2d;
  --white:#fff;
}
*{box-sizing:border-box;margin:0;padding:0}
html,body{width:1200px;height:2748px;overflow:hidden}
body{font-family:"Roboto",sans-serif;color:var(--text);background:var(--white);position:relative}
a{color:inherit;text-decoration:none}
.btn{display:inline-block;background:var(--green);color:var(--white);font-weight:700;font-size:13px;letter-spacing:.5px;text-transform:uppercase;padding:10px 22px;border-radius:20px}
.media{display:block}

/* header */
.site-header{position:absolute;top:0;left:0;width:1200px;height:108px;background:var(--white)}
.brand{position:absolute;left:170px;top:20px;display:flex;align-items:center;gap:10px}
.brand-mark{width:22px;height:22px;border-radius:50%;background:var(--green)}
.brand-name{font-size:34px;font-weight:700;color:var(--green);line-height:1}
.brand-sub{position:absolute;left:202px;top:58px;font-size:13px;color:var(--green);font-weight:400}
.topbar{position:absolute;right:172px;top:10px;display:flex;align-items:center;gap:12px}
.social{display:flex;gap:8px}
.social span{width:18px;height:18px;border-radius:50%;background:var(--green)}
.btn-top{padding:6px 18px;font-size:11px;border-radius:3px}
.main-nav{position:absolute;right:172px;top:58px;display:flex;gap:26px;font-size:14px;color:var(--ink)}
.main-nav a.active{color:var(--green)}

/* hero */
.hero{position:absolute;top:108px;left:0;width:1200px;height:324px;background:linear-gradient(90deg,#3a3a3a,#777 55%,#b9b4ad)}
.hero-figure{position:absolute;right:300px;top:0;width:300px;height:324px;background:linear-gradient(180deg,#d9c6b0,#c9b79f 60%,#eee)}
.hero-box{position:absolute;left:160px;top:28px;width:240px;height:300px;background:rgba(164,201,58,.94);padding:26px 22px;color:var(--white)}
.hero-box .kicker{font-size:12px;font-weight:500;text-transform:uppercase}
.hero-box h1{font-size:30px;font-weight:900;text-transform:uppercase;line-height:1.1;margin:6px 0 14px}
.hero-box p{font-size:12px;line-height:1.6}
.hero-box .btn{background:var(--white);color:var(--green);margin-top:28px;padding:7px 18px;font-size:11px}

/* about */
.about{position:absolute;top:432px;left:0;width:1200px;height:580px}
.about-photos{position:absolute;left:172px;top:170px;width:420px;height:392px}
.about-photos .p1{position:absolute;left:0;top:0;width:220px;height:392px;background:linear-gradient(160deg,#cfe2b7,#8aa36a)}
.about-photos .p2{position:absolute;left:220px;top:90px;width:200px;height:180px;background:radial-gradient(circle at 40% 40%,#f4a43a,#8fbf3a 60%,#6a8f2a)}
.about-text{position:absolute;left:618px;top:170px;width:380px}
.about-text .kicker{font-size:13px;font-weight:700;color:var(--blue);text-transform:uppercase}
.about-text h2{font-size:44px;font-weight:900;color:var(--ink);text-transform:uppercase;line-height:1}
.about-text .rule{width:40px;height:3px;background:var(--green);margin:10px 0 18px}
.about-text p{font-size:12.5px;line-height:1.7;margin-bottom:14px}
.about-text .btn{margin-top:10px}

/* services */
.services{position:absolute;top:1040px;left:0;width:1200px;height:600px;background:linear-gradient(180deg,#a9cc44,#92b935)}
.services h2{position:absolute;top:70px;width:100%;text-align:center;font-size:44px;font-weight:900;color:var(--white);text-transform:uppercase}
.services .rule{position:absolute;top:128px;left:580px;width:40px;height:3px;background:var(--white)}
.services .intro{position:absolute;top:146px;left:200px;width:800px;text-align:center;color:var(--white);font-size:12.5px;line-height:1.6}
.service-list{position:absolute;top:198px;left:172px;width:856px;display:flex;justify-content:space-between}
.service{width:272px;text-align:center;color:var(--white)}
.service .media{height:140px}
.service:nth-child(1) .media{background:linear-gradient(135deg,#e9e3dc,#a9a39a)}
.service:nth-child(2) .media{background:linear-gradient(135deg,#c4503a,#e8b452 60%,#7b9a3a)}
.service:nth-child(3) .media{background:linear-gradient(135deg,#f1ece6,#b8a998)}
.service h3{font-size:16px;font-weight:700;text-transform:uppercase;margin:14px 0 8px}
.service p{font-size:12px;line-height:1.6}
.service .btn{background:var(--white);color:var(--green);margin-top:16px;padding:7px 18px;font-size:11px}

/* booking */
.booking{position:absolute;top:1560px;left:172px;width:856px;height:408px;background:var(--white);box-shadow:0 4px 18px rgba(0,0,0,.12);padding:34px 70px}
.booking h2{text-align:center;font-size:40px;font-weight:900;color:var(--ink);text-transform:uppercase}
.booking .rule{width:40px;height:3px;background:var(--green);margin:8px auto 28px}
.form-row{display:flex;gap:16px;margin-bottom:14px}
.field{flex:1;height:40px;border:1px solid var(--line);font-size:12px;color:var(--muted);padding:12px}
.field.tall{height:76px}
.booking .btn{display:block;width:160px;margin:18px auto 0;text-align:center}

/* blog */
.blog{position:absolute;top:2000px;left:0;width:1200px;height:532px;background:var(--light)}
.blog .kicker{position:absolute;top:66px;width:100%;text-align:center;font-size:13px;font-weight:700;color:var(--ink);text-transform:uppercase}
.blog h2{position:absolute;top:82px;width:100%;text-align:center;font-size:44px;font-weight:900;color:var(--green);text-transform:uppercase}
.blog .rule{position:absolute;top:136px;left:580px;width:40px;height:3px;background:var(--green)}
.blog .intro{position:absolute;top:150px;left:220px;width:760px;text-align:center;font-size:12px;line-height:1.6}
.post-feature{position:absolute;top:200px;left:180px;width:412px;height:230px;background:var(--white);padding:20px;display:flex;gap:16px}
.post-feature .media{width:170px;height:190px;background:radial-gradient(circle at 50% 50%,#c7a15a,#7f9b3e 70%,#5a6e2c)}
.post-small{position:absolute;left:608px;width:412px;height:106px;background:var(--white);padding:12px;display:flex;gap:14px}
.post-small.a{top:200px}.post-small.b{top:322px}
.post-small .media{width:90px;height:82px;background:linear-gradient(135deg,#d6b07a,#8ca546)}
.post-small.b .media{background:linear-gradient(135deg,#e6d8c4,#a8b670)}
.post h4{font-size:15px;font-weight:700;color:var(--ink);margin-bottom:4px}
.post .meta{font-size:10.5px;color:var(--muted);margin-bottom:8px}
.post p{font-size:11.5px;line-height:1.55}

/* footer */
.site-footer{position:absolute;top:2532px;left:0;width:1200px;height:188px;background:var(--footer);color:#bbb;font-size:12px}
.footer-col{position:absolute;top:38px}
.footer-col h5{font-size:14px;font-weight:700;color:var(--white);text-transform:uppercase;margin-bottom:8px}
.footer-col .rule{width:30px;height:2px;background:var(--green);margin-bottom:14px}
.newsletter{left:172px;width:300px}
.newsletter .input{width:270px;height:30px;border-radius:15px;background:#444;color:#888;font-size:11px;padding:8px 14px}
.newsletter .btn{margin-top:10px;padding:6px 16px;font-size:10px;background:var(--blue)}
.links{left:520px;width:280px}
.links ul{list-style:none;columns:2;column-gap:20px}
.links li{margin-bottom:6px}
.contact{left:812px;width:220px;line-height:1.7}
.contact .social{margin-top:6px}
.contact .social span{width:14px;height:14px;background:#888}
.bottom-bar{position:absolute;top:2720px;left:0;width:1200px;height:28px;background:var(--blue);color:var(--white);font-size:10.5px;padding:8px 172px}
</style>
</head>
<body>

<header class="site-header">
  <div class="brand"><span class="brand-mark"></span><span class="brand-name">Verdant Fit</span></div>
  <div class="brand-sub">Nutritional Therapy</div>
  <div class="topbar">
    <div class="social"><span></span><span></span><span></span><span></span></div>
    <a class="btn btn-top" href="#booking">Book an Appointment</a>
  </div>
  <nav class="main-nav">
    <a class="active" href="#">Home</a><a href="#">Coaching / Fitness</a><a href="#">Naturopathy</a><a href="#">Personal Trainer</a><a href="#">Nutritional Supplement</a><a href="#">Contact Us</a>
  </nav>
</header>

<section class="hero">
  <div class="hero-figure" role="img" aria-label="Photo of a smiling woman in sportswear holding a smoothie in a gym"></div>
  <div class="hero-box">
    <div class="kicker">Welcome to</div>
    <h1>Verdant Fit</h1>
    <p>Coaching that brings nutrition, fitness and natural medicine together for a stronger, healthier you every day.</p>
    <a class="btn" href="#">Read More</a>
  </div>
</section>

<section class="about">
  <div class="about-photos">
    <div class="media p1" role="img" aria-label="Photos of a woman holding vegetables and a trainer coaching a client"></div>
    <div class="media p2" role="img" aria-label="Photo of fresh fruit and vegetables"></div>
  </div>
  <div class="about-text">
    <div class="kicker">Verdant Fit</div>
    <h2>About Us</h2>
    <div class="rule"></div>
    <p>Our studio brings together clinical nutritionists, naturopaths, rehab trainers, personal trainers and sport coaches under one roof, so every client gets a plan that fits body and life.</p>
    <p>We believe lasting health is built from good food, smart movement and steady support. Whether you are recovering from injury, training for a goal or simply wanting more energy, our team walks with you from the first session onward.</p>
    <a class="btn" href="#">Read More</a>
  </div>
</section>

<section class="services">
  <h2>Verdant Fit Work</h2>
  <div class="rule"></div>
  <p class="intro">From the kitchen to the gym floor, we coach whole families toward better health with care plans built around nutrition, natural medicine and athletic performance.</p>
  <div class="service-list">
    <div class="service">
      <div class="media" role="img" aria-label="Photo of a coaching fitness session"></div>
      <h3>Coaching Fitness</h3>
      <p>Guided training sessions that build strength, stamina and good habits for every level.</p>
      <a class="btn" href="#">Read More</a>
    </div>
    <div class="service">
      <div class="media" role="img" aria-label="Photo of healthy nutritional food"></div>
      <h3>Nutritional Medicine</h3>
      <p>Clinical nutrition plans that use real food to support energy, recovery and wellbeing.</p>
      <a class="btn" href="#">Read More</a>
    </div>
    <div class="service">
      <div class="media" role="img" aria-label="Photo of a rehab trainer working with a client"></div>
      <h3>Rehab Trainers</h3>
      <p>Careful rehab programs that restore movement and confidence after injury or surgery.</p>
      <a class="btn" href="#">Read More</a>
    </div>
  </div>
</section>

<section class="booking" id="booking">
  <h2>Online Booking</h2>
  <div class="rule"></div>
  <div class="form-row"><div class="field">Name</div><div class="field">Email</div></div>
  <div class="form-row"><div class="field">Phone</div></div>
  <div class="form-row"><div class="field tall">Message</div></div>
  <a class="btn" href="#">Submit</a>
</section>

<section class="blog">
  <div class="kicker">Recent Post</div>
  <h2>Blog Entries</h2>
  <div class="rule"></div>
  <p class="intro">Fresh ideas from our team on eating well, training smart and living naturally, shared every week for clients and families.</p>
  <article class="post post-feature">
    <div class="media" role="img" aria-label="Photo of a healthy salad bowl"></div>
    <div>
      <h4>Five foods for faster recovery</h4>
      <div class="meta">June 12, 2024 · 3 Comments</div>
      <p>Simple meals our nutritionists recommend after hard training days to rebuild muscle and restore energy.</p>
    </div>
  </article>
  <article class="post post-small a">
    <div class="media" role="img" aria-label="Photo of breakfast foods"></div>
    <div>
      <h4>Morning habits that last</h4>
      <div class="meta">June 8, 2024 · 2 Comments</div>
      <p>Small daily steps that set up a healthy, active day.</p>
    </div>
  </article>
  <article class="post post-small b">
    <div class="media" role="img" aria-label="Photo of herbal remedies"></div>
    <div>
      <h4>Herbs for better sleep</h4>
      <div class="meta">June 2, 2024 · 4 Comments</div>
      <p>Natural support from our naturopaths for deeper rest.</p>
    </div>
  </article>
</section>

<footer class="site-footer">
  <div class="footer-col newsletter">
    <h5>Newsletter Subscribe</h5><div class="rule"></div>
    <div class="input">Your email address</div>
    <a class="btn" href="#">Subscribe</a>
  </div>
  <div class="footer-col links">
    <h5>Useful Links</h5><div class="rule"></div>
    <ul><li>Home</li><li>Coaching Fitness</li><li>Naturopathy</li><li>Personal Trainer</li><li>Nutritional Supplement</li><li>Contact Us</li></ul>
  </div>
  <div class="footer-col contact">
    <h5>Contact Details</h5><div class="rule"></div>
    <div>+61 2 5550 1234</div>
    <div>hello@verdantfit.example</div>
    <div>14 Fernleaf Road, Greenvale NSW</div>
    <div class="social"><span></span><span></span><span></span><span></span></div>
  </div>
</footer>
<div class="bottom-bar">© 2024 Verdant Fit. All rights reserved.</div>

</body>
</html>
```